Employee Portal UI Design - Modern and Clean

We are an agency tasked with developing a team portal for a company that has many employees. As we embark on this project, we seek a great UI design to accompany the requirements our client has for this project. We already have several screens mocked up that can be used as reference for the overall idea. Currently, we are only looking for the main dashboard's home page, user registration screen, and account settings page to be designed. The main brand colors are red but other accents can be used as well. The client's vision is for modern & minimalist to be at the center. We have a specific font to be used, but if you don't have access to it, you can just use a similar font.Main color: #DD0031The sub menus (do not need to be designed) would be:>Performance Reviews>Posts>Team directory>Calendar>Tasks>Documents>LinksWe would prefer the design be made in Adobe XD.

Industry/Entity Type

Fast Food Restaurant

Number of Pages Required

1 page

Font styles to use
Sans Serif

Colors
ec1f27

Requirements
Must have
• Color: #DD0031 (highlights)

```html
<!DOCTYPE html>
<html lang="en">
<head>
<meta charset="utf-8">
<title>Crewdash – Dashboard</title>
<link href="https://fonts.googleapis.com/css2?family=Lato:ital,wght@0,300;0,400;0,700;0,900;1,700&display=swap" rel="stylesheet">
<style>
:root{
  --red:#ec1f27;
  --navy:#2e2e3e;
  --ink:#2f3040;
  --muted:#7b7e91;
  --band:#dfe0e4;
  --pale:#f2f3f5;
  --white:#ffffff;
  --chip:#b4b6c2;
}
*{box-sizing:border-box;margin:0;padding:0}
html,body{width:1200px;height:1200px;overflow:hidden}
body{position:relative;font-family:'Lato',sans-serif;color:var(--ink);background:var(--white)}
.abs{position:absolute}

/* header */
.topbar{position:absolute;left:0;top:0;width:1200px;height:80px;background:var(--navy);border-top:4px solid var(--red)}
.menu-toggle{position:absolute;left:38px;top:32px;width:24px}
.menu-toggle span{display:block;height:3px;background:var(--white);margin-bottom:4px}
.menu-toggle::after{content:"";position:absolute;left:7px;top:28px;border:5px solid transparent;border-top:5px solid var(--red)}
.brand{position:absolute;left:99px;top:24px;font-size:29px;font-weight:700;color:var(--white);letter-spacing:-0.5px}
.user-avatar{position:absolute;left:752px;top:18px;width:40px;height:40px;border-radius:50%;background:#6b6d80}
.login-label{position:absolute;left:803px;top:22px;font-size:10.5px;font-weight:700;letter-spacing:2.2px;color:#c9cad3}
.login-name{position:absolute;left:803px;top:38px;font-size:16px;font-weight:700;font-style:italic;color:var(--red)}
.logout{position:absolute;left:1001px;top:34px;font-size:10.5px;font-weight:700;letter-spacing:2.4px;color:var(--red)}
.vline{position:absolute;top:25px;width:1px;height:30px;background:#565869}
.bell{position:absolute;left:1085px;top:28px}
.badge{position:absolute;left:1096px;top:23px;width:14px;height:14px;border-radius:50%;background:var(--red);color:#fff;font-size:9px;font-weight:700;text-align:center;line-height:14px}
.gear{position:absolute;left:1132px;top:32px}

/* band */
.band{position:absolute;left:0;top:80px;width:1200px;height:96px;background:var(--band)}
.page-tab{position:absolute;left:104px;top:112px;width:448px;height:64px;background:var(--white)}
.page-title{position:absolute;left:136px;top:127px;font-size:30px;font-weight:300;color:var(--ink)}
.btn{display:block;position:absolute;background:var(--red);color:#fff;font-size:11px;font-weight:900;letter-spacing:2.5px;text-align:center;border-radius:2px}
.btn-new{left:456px;top:127px;width:80px;height:32px;line-height:32px;padding-right:14px}
.btn-new::after{content:"+";position:absolute;right:13px;top:-1px;font-size:17px;font-weight:400;letter-spacing:0}
.search{position:absolute;left:848px;top:111px;width:304px;height:35px;background:var(--white);border-radius:2px}
.search svg{position:absolute;right:11px;top:9px}

/* posts */
.post{position:absolute;left:104px;width:624px;height:300px}
.post-avatar{position:absolute;left:0;top:0;width:64px;height:64px;border-radius:50%;background:#6b6d80;overflow:hidden}
.post-author{position:absolute;left:86px;top:6px;font-size:24px;font-weight:700;font-style:italic;color:var(--red);letter-spacing:-0.3px}
.post-meta{position:absolute;left:86px;top:37px;font-size:18px;font-weight:300;color:var(--muted)}
.post-meta b{font-weight:400;color:var(--ink)}
.post-posted{position:absolute;right:2px;top:23px;font-size:10.5px;font-weight:900;letter-spacing:2px;color:var(--muted)}
.post-time{position:absolute;right:2px;top:37px;font-size:13px;color:var(--ink)}
.post-body{position:absolute;left:-1px;top:80px;width:622px;font-size:14.4px;line-height:23px;color:var(--ink)}
.btn-more{left:0;top:215px;width:112px;height:32px;line-height:32px}
.post-rule{position:absolute;left:0;top:275px;width:624px;height:2px;background:#e3e4e8}

/* sidebar */
.side{position:absolute;left:800px;width:400px}
.events{top:176px;height:272px;background:var(--pale)}
.tasks{top:448px;height:416px;background:var(--band)}
.polls{top:864px;height:272px;background:var(--pale)}
.side h2{position:absolute;left:46px;font-size:26px;font-weight:300;color:var(--ink)}
.view-all{position:absolute;right:48px;font-size:11px;font-weight:900;letter-spacing:2.6px;color:var(--red)}
.row{position:absolute;left:48px;height:34px;width:340px}
.row svg{position:absolute;left:0;top:2px}
.ev-date{position:absolute;left:38px;top:6px;font-size:16px;color:var(--ink)}
.sep{position:absolute;top:1px;width:2px;height:32px;background:#b9bbc6}
.ev-title{position:absolute;left:110px;top:-1px;font-size:14.4px;color:var(--ink)}
.ev-sub{position:absolute;left:110px;top:20px;font-size:10.5px;color:var(--ink)}
.day{position:absolute;left:47px;font-size:12px;font-weight:700;color:var(--muted)}
.tk-time{position:absolute;left:42px;top:6px;font-size:16px;color:var(--ink)}
.tk-title{position:absolute;left:130px;top:7px;font-size:14.4px;color:var(--ink)}
.tk-rule{position:absolute;left:48px;top:226px;width:304px;height:1px;background:#b9bbc6}
.question{position:absolute;left:47px;top:75px;font-size:14.4px;font-weight:700;color:var(--ink);letter-spacing:-0.2px}
.option{position:absolute;left:48px;width:304px;height:32px;line-height:32px;padding-left:12px;font-size:14.4px;border-radius:2px}
.opt-a{top:108px;background:var(--chip);color:#eef0f4}
.opt-b{top:152px;background:var(--navy);color:#fff}
.btn-vote{left:48px;top:196px;width:120px;height:32px;line-height:32px}

/* footer */
.footer{position:absolute;left:0;top:1136px;width:1200px;height:64px;background:var(--navy);color:#fff;font-size:10px}
.footer .l{position:absolute;left:103px;top:26px}
.footer .r{position:absolute;right:44px;top:26px}
.footer .r a{color:var(--red);font-weight:700;text-decoration:none}
</style>
</head>
<body>

<svg width="0" height="0" style="position:absolute">
  <defs>
    <symbol id="cal" viewBox="0 0 26 26">
      <rect x="1" y="4" width="24" height="21" rx="2" fill="none" stroke="#7b7e91" stroke-width="1.6"/>
      <rect x="1" y="4" width="24" height="5" fill="#7b7e91"/>
      <rect x="6" y="1" width="2" height="5" fill="#7b7e91"/><rect x="18" y="1" width="2" height="5" fill="#7b7e91"/>
      <g fill="#7b7e91"><rect x="6" y="12" width="3" height="3"/><rect x="11.5" y="12" width="3" height="3"/><rect x="17" y="12" width="3" height="3"/><rect x="6" y="18" width="3" height="3"/><rect x="11.5" y="18" width="3" height="3"/><rect x="17" y="18" width="3" height="3"/></g>
    </symbol>
    <symbol id="task" viewBox="0 0 36 32">
      <rect x="1" y="1" width="22" height="30" fill="none" stroke="#7b7e91" stroke-width="1.6"/>
      <g stroke="#7b7e91" stroke-width="2"><line x1="5" y1="7" x2="19" y2="7"/><line x1="5" y1="12" x2="19" y2="12"/><line x1="5" y1="17" x2="19" y2="17"/><line x1="5" y1="22" x2="17" y2="22"/><line x1="5" y1="27" x2="15" y2="27"/></g>
      <path d="M20 24 L32 8 L35 10 L23 26 L19 28 Z" fill="#dfe0e4" stroke="#7b7e91" stroke-width="1.3"/>
    </symbol>
    <symbol id="person" viewBox="0 0 64 64">
      <circle cx="32" cy="22" r="11" fill="#b4b6c2"/>
      <path d="M14 54 C14 40 22 35 32 35 C42 35 50 40 50 54 Z" fill="#b4b6c2"/>
    </symbol>
  </defs>
</svg>

<header class="topbar">
  <div class="menu-toggle"><span></span><span></span><span></span></div>
  <div class="brand">Crewdash</div>
  <div class="user-avatar"><svg width="40" height="40"><use href="#person"/></svg></div>
  <div class="login-label">YOU ARE LOGGED IN AS</div>
  <div class="login-name">Daniel Mercer</div>
  <div class="logout">LOGOUT</div>
  <div class="vline" style="left:1070px"></div>
  <svg class="bell" width="22" height="24" viewBox="0 0 22 24"><path d="M4 18 V10 A7 7 0 0 1 18 10 V18 L20 20 H2 Z" fill="none" stroke="#9a9cab" stroke-width="1.5"/><path d="M9 21 A2 2 0 0 0 13 21" fill="none" stroke="#9a9cab" stroke-width="1.5"/></svg>
  <div class="badge">2</div>
  <div class="vline" style="left:1118px"></div>
  <svg class="gear" width="20" height="20" viewBox="0 0 20 20"><circle cx="10" cy="10" r="3" fill="none" stroke="#9a9cab" stroke-width="1.5"/><path d="M10 1.5 L12 3.5 L14.8 3 L15.5 5.7 L18 7 L17 9.7 L18.5 12 L16.2 13.6 L16 16.4 L13.2 16.6 L11.5 18.7 L9 17.5 L6.5 18.7 L5 16.4 L2.2 16 L2.7 13.2 L1 11 L2.8 8.8 L2.2 6 L5 5.2 L6 2.5 L8.7 3 Z" fill="none" stroke="#9a9cab" stroke-width="1.4" stroke-linejoin="round"/></svg>
</header>

<div class="band"></div>
<div class="page-tab"></div>
<h1 class="page-title">Recent Activities</h1>
<a class="btn btn-new">NEW</a>
<div class="search"><svg width="18" height="18" viewBox="0 0 18 18"><circle cx="10.5" cy="7.5" r="5.5" fill="none" stroke="#2f3040" stroke-width="1.8"/><line x1="6.5" y1="11.5" x2="2" y2="16" stroke="#2f3040" stroke-width="2.2"/></svg></div>

<main>
  <article class="post" style="top:217px">
    <div class="post-avatar"><svg width="64" height="64"><use href="#person"/></svg></div>
    <div class="post-author">Daniel Mercer</div>
    <div class="post-meta">Public post for <b>Team Leaders</b></div>
    <div class="post-posted">POSTED</div>
    <div class="post-time">Today - 10:15</div>
    <p class="post-body">Lorem ipsum dolor sit amet, consectetur adipiscing elit, sed do eiusmod tempor incididunt ut labore et dolore magna aliqua. Ut enim ad minim veniam, quis nostrud exercitation ullamco laboris nisi ut aliquip ex ea commodo consequat. Duis aute irure dolor in reprehenderit in voluptate velit esse cillum dolore eu fugiat nulla pariatur. Excepteur sint occaecat cupidatat non proident, sunt in culpa qui officia deserunt mollit anim id est laborum.</p>
    <a class="btn btn-more">READ MORE</a>
    <div class="post-rule"></div>
  </article>
  <article class="post" style="top:517px">
    <div class="post-avatar"><svg width="64" height="64"><use href="#person"/></svg></div>
    <div class="post-author">Daniel Mercer</div>
    <div class="post-meta">Public post for <b>Team Leaders</b></div>
    <div class="post-posted">POSTED</div>
    <div class="post-time">Today - 10:15</div>
    <p class="post-body">Lorem ipsum dolor sit amet, consectetur adipiscing elit, sed do eiusmod tempor incididunt ut labore et dolore magna aliqua. Ut enim ad minim veniam, quis nostrud exercitation ullamco laboris nisi ut aliquip ex ea commodo consequat. Duis aute irure dolor in reprehenderit in voluptate velit esse cillum dolore eu fugiat nulla pariatur. Excepteur sint occaecat cupidatat non proident, sunt in culpa qui officia deserunt mollit anim id est laborum.</p>
    <a class="btn btn-more">READ MORE</a>
    <div class="post-rule"></div>
  </article>
  <article class="post" style="top:817px">
    <div class="post-avatar"><svg width="64" height="64"><use href="#person"/></svg></div>
    <div class="post-author">Daniel Mercer</div>
    <div class="post-meta">Public post for <b>Team Leaders</b></div>
    <div class="post-posted">POSTED</div>
    <div class="post-time">Today - 10:15</div>
    <p class="post-body">Lorem ipsum dolor sit amet, consectetur adipiscing elit, sed do eiusmod tempor incididunt ut labore et dolore magna aliqua. Ut enim ad minim veniam, quis nostrud exercitation ullamco laboris nisi ut aliquip ex ea commodo consequat. Duis aute irure dolor in reprehenderit in voluptate velit esse cillum dolore eu fugiat nulla pariatur. Excepteur sint occaecat cupidatat non proident, sunt in culpa qui officia deserunt mollit anim id est laborum.</p>
    <a class="btn btn-more">READ MORE</a>
  </article>
</main>

<aside>
  <section class="side events">
    <h2 style="top:27px">Events</h2>
    <div class="view-all" style="top:43px">VIEW ALL EVENTS</div>
    <div class="row" style="top:80px"><svg width="26" height="26"><use href="#cal"/></svg><span class="ev-date">18 Jan</span><span class="sep" style="left:96px"></span><span class="ev-title">Directors Meeting</span><span class="ev-sub">Restaurant | 10:00am - 11:00am</span></div>
    <div class="row" style="top:136px"><svg width="26" height="26"><use href="#cal"/></svg><span class="ev-date">18 Jan</span><span class="sep" style="left:96px"></span><span class="ev-title">Directors Meeting</span><span class="ev-sub">Restaurant | 10:00am - 11:00am</span></div>
    <div class="row" style="top:192px"><svg width="26" height="26"><use href="#cal"/></svg><span class="ev-date">18 Jan</span><span class="sep" style="left:96px"></span><span class="ev-title">Directors Meeting</span><span class="ev-sub">Restaurant | 10:00am - 11:00am</span></div>
  </section>

  <section class="side tasks">
    <h2 style="top:27px">Tasks</h2>
    <div class="view-all" style="top:43px;right:57px">VIEW ALL TASKS</div>
    <div class="day" style="top:80px">TOMORROW:</div>
    <div class="row" style="top:112px"><svg width="36" height="32"><use href="#task"/></svg><span class="tk-time">8.45pm</span><span class="sep" style="left:116px"></span><span class="tk-title">Task title in here</span></div>
    <div class="row" style="top:168px"><svg width="36" height="32"><use href="#task"/></svg><span class="tk-time">9.15pm</span><span class="sep" style="left:116px"></span><span class="tk-title">Task title in here</span></div>
    <div class="tk-rule"></div>
    <div class="day" style="top:244px">FRIDAY:</div>
    <div class="row" style="top:276px"><svg width="36" height="32"><use href="#task"/></svg><span class="tk-time">8.45pm</span><span class="sep" style="left:116px"></span><span class="tk-title">Task title in here</span></div>
    <div class="row" style="top:332px"><svg width="36" height="32"><use href="#task"/></svg><span class="tk-time">9.15pm</span><span class="sep" style="left:116px"></span><span class="tk-title">Task title in here</span></div>
  </section>

  <section class="side polls">
    <h2 style="top:27px">Polls</h2>
    <div class="view-all" style="top:43px;right:58px">VIEW ALL POLLS</div>
    <div class="question">Lorem ipsum dolor sit amet adipiscing elit?</div>
    <div class="option opt-a">Quis nostrud ullamco laboris nisi aliquip.</div>
    <div class="option opt-b">Consequat duis aute irure dolor in reprehe</div>
    <a class="btn btn-vote">SUBMIT VOTE</a>
  </section>
</aside>

<footer class="footer">
  <span class="l">Lorem ipsum dolor sit amet, consectetur adipiscing elit, sed do eiusmod tempor incididunt ut labore et dolore magna aliqua.</span>
  <span class="r">Sunt in culpa qui officia deserunt mollit &nbsp;| &nbsp;<a>Link in here</a></span>
</footer>

</body>
</html>
```